Professional Learning Organization for Educators needs a Design Thinking Workshop Flyer

We need a flyer for a series of Introductory Design Thinking workshops we're delivering for education leaders.

We have generated our own version of the flyer with a word template, but want it to look even more professional and eye catching. It is attached.

We had an image that we thought might be good, but pulled it out so we don't bias designers' thinking.
Updates

Reason: We are a bit flexible on the deadline since this is a holiday week and people are traveling

Target Market(s)

Very busy education leaders whose curiosity needs to be stimulated enough to enroll in the course

Industry/Entity Type

Education

Font styles to use
Other font styles liked:
• Century Gothic or something closer to that

Requirements
Must have
• Some version of the text that is on the current flyer that I attached.
Nice to have
• I am very flexible and open right now on this design.

```html
<!DOCTYPE html>
<html lang="en">
<head>
<meta charset="utf-8">
<title>Design Thinking Workshops Flyer</title>
<link rel="stylesheet" href="https://fonts.googleapis.com/css2?family=Didact+Gothic&family=Jost:wght@500;600;700&family=Oswald:wght@500;600;700&display=swap">
<style>
  :root {
    --blue: #1a4fa3;
    --teal: #2a9ea3;
    --teal-dark: #237f88;
    --teal-text: #2597a0;
    --ink: #2b2b2b;
    --paper: #ffffff;
    --backdrop: #e9e9e9;
    --photo-light: #e8ddd0;
    --photo-dark: #c9b39c;
    --quote-mark: rgba(255, 255, 255, 0.28);
  }
  * { margin: 0; padding: 0; box-sizing: border-box; }
  html, body { width: 1000px; height: 1200px; overflow: hidden; }
  body { background: var(--backdrop); position: relative; }

  .flyer {
    position: absolute;
    left: 90px;
    top: 21px;
    width: 620px;
    height: 876px;
    background: var(--paper);
    transform: scale(1.3226);
    transform-origin: top left;
    overflow: hidden;
    font-family: "Didact Gothic", "Century Gothic", sans-serif;
    color: var(--ink);
  }

  .hero-photo {
    position: absolute;
    left: 0; top: 0;
    width: 620px; height: 400px;
    background: linear-gradient(180deg, var(--photo-light) 0%, var(--photo-dark) 100%);
  }

  .shapes { position: absolute; left: 0; top: 0; }
  .abs { position: absolute; }

  /* Left column */
  .headline {
    left: 0; top: 348px; width: 328px;
    text-align: right;
    font-family: "Jost", sans-serif;
    font-weight: 700;
    font-size: 31px;
    color: var(--teal-text);
    line-height: 1;
  }
  .subhead {
    left: 0; top: 388px; width: 328px;
    text-align: right;
    font-family: "Jost", sans-serif;
    font-weight: 700;
    font-size: 17px;
    color: var(--teal-text);
  }
  .intro {
    left: 46px; top: 427px; width: 282px;
    font-size: 11px;
    line-height: 15px;
    text-align: justify;
  }
  .benefits { list-style: none; margin-top: 8px; }
  .benefits li {
    position: relative;
    padding-left: 14px;
    margin-bottom: 6px;
    text-align: left;
  }
  .benefits .tick {
    position: absolute; left: 0; top: 3px;
    width: 10px; height: 9px;
  }
  .intro p + p { margin-top: 10px; }
  .offer { font-size: 12px; line-height: 16px; }

  .schedule {
    left: 46px; top: 674px;
    border-collapse: collapse;
    font-size: 12.5px;
  }
  .schedule td { padding: 0 0 4px 0; line-height: 15px; }
  .schedule .session { color: var(--teal-text); width: 154px; white-space: nowrap; }
  .schedule .dates { color: var(--ink); white-space: nowrap; }

  .cta {
    left: 0; top: 788px; width: 320px;
    text-align: right;
    font-family: "Jost", sans-serif;
    font-weight: 700;
    font-size: 22px;
    line-height: 27px;
    color: #fff;
  }
  .cta-note {
    left: 43px; top: 847px;
    font-size: 14px;
    color: #fff;
  }

  /* Right column */
  .title-block {
    left: 362px; top: 262px; width: 240px;
    transform: rotate(-7deg);
    transform-origin: left top;
    color: #fff;
    font-family: "Oswald", sans-serif;
    font-weight: 700;
    line-height: 0.95;
  }
  .title-main { font-size: 72px; letter-spacing: 0.5px; display: block; }
  .title-sub { font-size: 20px; font-weight: 600; display: block; margin-top: 1px; }

  .testimonials {
    left: 366px; top: 403px; width: 218px;
    color: #fff;
    text-align: center;
  }
  .testimonials h2 {
    font-family: "Didact Gothic", sans-serif;
    font-weight: 400;
    font-size: 17px;
    line-height: 21px;
    letter-spacing: 0.3px;
    margin-bottom: 24px;
  }
  .quote {
    position: relative;
    font-size: 11.5px;
    line-height: 15px;
    padding: 0 16px;
    margin-bottom: 22px;
  }
  .quote::before, .quote::after {
    position: absolute;
    font-family: "Jost", sans-serif;
    font-weight: 700;
    font-size: 40px;
    line-height: 1;
    color: var(--quote-mark);
  }
  .quote::before { content: "\201C"; left: -4px; top: -8px; }
  .quote::after { content: "\201D"; right: -4px; bottom: -24px; }

  .contact {
    left: 348px; top: 730px; width: 248px;
    text-align: center;
    color: #fff;
  }
  .org-name {
    font-family: "Oswald", sans-serif;
    font-weight: 600;
    font-size: 22px;
    letter-spacing: 0.3px;
    line-height: 32px;
  }
  .contact-line { font-size: 17px; line-height: 31px; }
  .contact-question {
    font-family: "Jost", sans-serif;
    font-weight: 700;
    font-size: 17px;
    line-height: 30px;
  }
</style>
</head>
<body>
  <main class="flyer">
    <div class="hero-photo" role="img" aria-label="Photo of children painting at easels in a bright art classroom"></div>

    <svg class="shapes" width="620" height="876" viewBox="0 0 620 876" aria-hidden="true">
      <polygon points="0,366 348,288 348,876 0,876" fill="var(--paper)"/>
      <rect x="596" y="290" width="24" height="420" fill="var(--paper)"/>
      <polygon points="348,258 596,203 596,350 348,398" fill="var(--blue)"/>
      <polygon points="348,398 596,350 596,876 348,876" fill="var(--teal)"/>
      <polygon points="596,708 620,700 620,876 596,876" fill="var(--blue)"/>
      <polygon points="0,752 60,752 215,789 0,792" fill="var(--teal-dark)"/>
      <polygon points="0,792 348,758 348,876 0,876" fill="var(--blue)"/>
    </svg>

    <h1 class="abs headline">Designing</h1>
    <p class="abs subhead">Your Way To Better Solutions</p>

    <div class="abs intro">
      <p>Maple Ridge Public Schools and Summit Valley BOCES invite you to discover the power of Design Thinking. During our three session course, you will learn and practice mindsets and tools that help you continuously and creatively improve the experiences of the people you serve by:</p>
      <ul class="benefits">
        <li><svg class="tick" viewBox="0 0 10 9"><path d="M1 4.5 L4 7.5 L9 1" fill="none" stroke="var(--teal-text)" stroke-width="1.6"/></svg>Understanding what your teachers, students and community truly need in their learning and work experiences</li>
        <li><svg class="tick" viewBox="0 0 10 9"><path d="M1 4.5 L4 7.5 L9 1" fill="none" stroke="var(--teal-text)" stroke-width="1.6"/></svg>Designing solutions that better meet their needs</li>
        <li><svg class="tick" viewBox="0 0 10 9"><path d="M1 4.5 L4 7.5 L9 1" fill="none" stroke="var(--teal-text)" stroke-width="1.6"/></svg>Seeking authentic feedback and reactions to these solutions prior to their implementation.</li>
      </ul>
      <p class="offer">We are offering this three-session course at four different times in spring semester. Please choose the course that works best for your schedule.</p>
    </div>

    <table class="abs schedule">
      <tr><td class="session">Monday Mornings:</td><td class="dates">1/23, 1/30 and 2/6</td></tr>
      <tr><td class="session">Tuesday Afternoons:</td><td class="dates">2/7, 2/14 and 2/21</td></tr>
      <tr><td class="session">Wednesday Afternoons:</td><td class="dates">3/8, 3/15 and 3/22</td></tr>
      <tr><td class="session">Wednesday Evenings:</td><td class="dates">2/8, 2/15 and 2/22</td></tr>
    </table>

    <p class="abs cta">CLICK<br>HERE TO ENROLL</p>
    <p class="abs cta-note">Go to www.svboces.org to learn more</p>

    <div class="abs title-block">
      <span class="title-main">DESIGN</span>
      <span class="title-sub">THINKING WORKSHOPS</span>
    </div>

    <section class="abs testimonials">
      <h2>WHAT OUR<br>PARTICIPANTS SAY…</h2>
      <p class="quote">This has been an empowering experience that allowed me to try out dramatic changes in my practice that I wouldn’t have imagined before.</p>
      <p class="quote">I never realized how often I’ve guessed and assumed what our teachers and students need – now I have a way to stop guessing!</p>
      <p class="quote">I finally have tools to generate truly creative ideas that people actually embrace… because they meet their needs</p>
    </section>

    <div class="abs contact">
      <p class="org-name">SUMMIT VALLEY BOCES</p>
      <p class="contact-line">www.svboces.org</p>
      <p class="contact-question">Questions?</p>
      <p class="contact-line">J.Carter@svlearn.org</p>
    </div>
  </main>
</body>
</html>
```